Sunporch Tidy Works half fold brochure design

I need a brochure for a new company. The name of the company is Sunporch Tidy Works. I am a Professional Organizer. I am requesting a one fold brochure 11" wide x 8.5" high (obviously once folded 5.5" wide x 8.5" high) brochure. I have been told this may need to be designed as a flyer? I have attached a VERY BASIC layout of what I think I am looking for. I have also attached the original logos in all the different formats I have. I would like to have a very light green background & the text I have in orange please make orange. PLEASE feel free to add color to my "Sunporch Tidy Works" logo's and use light/soft green & orange shades if possible (OK to go darker for BOLD purposes) The brochure DOES NOT have to stick to this layout, again just what I THINK I want :) - THANK YOU

EDIT: 01-21-15 Remove MARGARET BELDANE from all 3 places (front, bottom inside right & back) Remove just the BELDANE from the 1st line on the back. PRIVACY & ETHICS on the back, please remove "PRIVACY &", leave Ethics and the 1st line of the text under it. Please remove all of the text following the 1st sentence. THANK YOU

```html
<!DOCTYPE html>
<html lang="en">
<head>
<meta charset="utf-8">
<title>Sunporch Tidy Works – Half Fold Brochure</title>
<link rel="stylesheet" href="https://fonts.googleapis.com/css2?family=Arimo:ital,wght@0,400;0,700;1,400&display=swap">
<style>
  :root {
    --ink: #111111;
    --orange: #f07a22;
    --orange-deep: #e2661a;
    --green-soft: #a9d89a;
    --green-pale: #e9f5e3;
    --paper: #ffffff;
    --stage: #ffffff;
    --frame: #000000;
    --seal: #cfd8cb;
  }
  * { box-sizing: border-box; margin: 0; padding: 0; }
  html, body {
    width: 1200px; height: 900px; overflow: hidden;
    background: var(--stage);
    font-family: "Arimo", Arial, sans-serif;
    color: var(--ink);
  }
  .canvas { position: relative; width: 1200px; height: 900px; }

  .sheet {
    position: absolute; width: 580px; height: 448px;
    border: 3px solid var(--frame);
    display: flex; overflow: hidden;
  }
  .sheet--outside { left: 10px; top: 10px; background: var(--paper); }
  .sheet--inside {
    left: 610px; top: 442px;
    background: radial-gradient(ellipse 60% 70% at 50% 45%, var(--paper) 0%, var(--green-pale) 55%, var(--green-soft) 100%);
  }
  .panel { width: 50%; height: 100%; position: relative; }

  /* wordmark */
  .wordmark { display: flex; align-items: center; gap: 5px; justify-content: center; }
  .wordmark__square { width: 14px; height: 14px; background: var(--orange); }
  .wordmark__name { font-weight: 700; color: var(--orange-deep); font-size: 15px; }

  /* back panel */
  .back {
    background: linear-gradient(90deg, var(--green-soft) 0%, var(--green-pale) 45%, var(--paper) 100%);
    text-align: center; padding: 62px 24px 0 24px;
    font-size: 8.5px; line-height: 1.55;
  }
  .back .wordmark { margin-bottom: 22px; }
  .back__service { font-weight: 700; margin-bottom: 10px; }
  .back__contact { font-weight: 700; }
  .seal {
    width: 64px; height: 64px; border-radius: 4px;
    background: var(--seal); margin: 24px auto 18px;
  }
  .privacy { font-weight: 700; font-size: 8.5px; line-height: 1.35; }

  /* front panel */
  .front { text-align: center; padding: 20px 14px 0 14px; }
  .front .wordmark { justify-content: flex-end; margin-bottom: 24px; }
  .front__title { font-size: 19px; font-weight: 700; line-height: 1.25; }
  .front__area { font-size: 10px; font-weight: 700; margin-top: 6px; }
  .front__art {
    width: 220px; height: 150px; margin: 14px auto 12px; border-radius: 10px;
    background: radial-gradient(circle at 50% 50%, #c9c7e6 0%, #e6e6f2 45%, var(--paper) 80%);
  }
  .front__tagline { color: var(--orange); font-size: 11.5px; margin-bottom: 6px; }
  .front__contact { font-size: 11px; line-height: 1.35; }

  /* inside */
  .inside { padding: 12px 14px 10px; font-size: 7.4px; line-height: 1.32; }
  .inside p { margin-bottom: 7px; }
  .inside h2 { color: var(--orange); font-weight: 400; font-size: 10.5px; text-align: center; margin-bottom: 3px; }
  .inside h2.bold { font-weight: 700; }
  .inside .lead { font-weight: 700; text-align: center; }
  .divider { border: 0; border-top: 2px dotted var(--orange); width: 45%; margin: 4px auto 8px; }
  .closing {
    color: var(--orange); font-weight: 700; font-size: 8.5px; text-align: center;
    line-height: 1.5; margin-top: 22px;
  }
  .quote { text-align: center; }
  .services {
    background: var(--paper); border: 1px solid var(--ink);
    display: flex; gap: 12px; padding: 7px 8px; font-size: 6.6px; line-height: 1.3; margin-top: 6px;
  }
  .services__col { flex: 1; }
  .services h3 { font-size: 6.6px; font-weight: 700; margin-top: 5px; }
  .services h3:first-child { margin-top: 0; }
  .services ul { list-style: none; }
  .services li::before { content: "• "; }
  .services .note { font-weight: 700; margin-top: 6px; }
</style>
</head>
<body>
<main class="canvas">

  <section class="sheet sheet--outside" aria-label="Brochure outside: back and front cover">
    <div class="panel back">
      <div class="wordmark"><span class="wordmark__square"></span><span class="wordmark__name">Sunporch Tidy Works</span></div>
      <p class="back__service">Organizing &amp; Decluttering Services</p>
      <p class="back__contact">301-555-0148<br>info@sunporchtidyworks.com<br>www.sunporchtidyworks.com<br>Fairbrook, MD</p>
      <div class="seal" role="img" aria-label="Membership seal"></div>
      <p class="privacy">PRIVACY:<br>I abide by the standards as outlined in the Guild Code of Ethics. Any and all information provided by you, as well as information or circumstances seen on site will be handled in a nonjudgmental, respectful and confidential manner.</p>
    </div>
    <div class="panel front">
      <div class="wordmark"><span class="wordmark__square"></span><span class="wordmark__name">Sunporch Tidy Works</span></div>
      <h1 class="front__title">Organizing &amp; Decluttering<br>Services</h1>
      <p class="front__area">Serving MD, DC, &amp; VA</p>
      <div class="front__art" role="img" aria-label="Illustration of a house with a peace sign linked to a calendar, file trays, a trash can and a moving box"></div>
      <p class="front__tagline">Clarity: “The Quality or State of Being Clear”</p>
      <p class="front__contact">301-555-0148<br>info@sunporchtidyworks.com<br>www.sunporchtidyworks.com</p>
    </div>
  </section>

  <section class="sheet sheet--inside" aria-label="Brochure inside spread">
    <div class="panel inside">
      <h2>Nice to Meet You</h2>
      <p>Hello! My name is Margaret. I offer simple, fun and insightful solutions to seemingly complicated clutter and organizational problems. I am here to help if you are ready to change your home and/or workspace!</p>
      <p>My experiences of working with family, friends, co-workers and clients have proven my hard working, energetic, fun and supportive attitude make it easier for them to get things accomplished. Helping people sort through, and be rid of, the mental and physical obstacles that have kept them stuck, along with participating in their enthusiasm when they see immediate improvement, is rewarding for me.</p>
      <p>I welcome the opportunity to earn your confidence through ethical, reliable and dependable hard work</p>
      <hr class="divider">
      <p class="lead">Getting organized isn’t all about everything being in its proper place. It can also require overcoming fears and anxieties such as:</p>
      <h2>“How do I start?”</h2>
      <p>You begin by getting help from a professional. No one can do everything; everyone needs a helping hand at times. For example, I bring my vehicle to a mechanic when it needs service, even for just a simple oil change!</p>
      <h2>“Am I going to have to get rid of ALL my things?”</h2>
      <p>Absolutely not! There is a process that will help you decide what to keep and what you would be willing to part with. (I can help you determine the practical and monetary “worth” of something. Only you can determine its personal “value”.)</p>
      <p class="closing">TOGETHER WE CAN CONQUER THE CLUTTER<br>AND CREATE CLARITY!</p>
    </div>
    <div class="panel inside">
      <h2>“I don’t have time”</h2>
      <p>Now you will! Getting organized will actually save you time. You will know where that “thing” is, find it quickly and avoid the time it takes to run out and purchase a new “thing”. (You will have actually created more time to enjoy the lifestyle that is important to you.)</p>
      <hr class="divider">
      <p class="lead">We all have anxiety about something that prevents or inhibits us from taking action toward a solution. Whether you want someone to take over the project or a helping hand (nudge) is all you really need, a professional organizer is the perfect way to get started. Getting organized is going to be a process of progress, not perfection. It will require some level of support and continued work on you part, but the rewards will far outweigh the efforts.</p>
      <h2 class="bold">What is a professional organizer?</h2>
      <p class="quote">“A Professional Organizer enhances the lives of clients by designing systems and processes using organizing principles and through transferring organizing skills. Professional Organizers help individuals and businesses take control of their surroundings, their time, their paper, and their systems for life.” – Guild of Home Organizers</p>
      <p class="quote">Whether you are too busy, too confused, over whelmed, tired, stressed or just don’t know where to start, I offer a variety of hands on services to help you bring a sense of fun, freedom and functionality to almost any space.</p>
      <div class="services">
        <div class="services__col">
          <h3>ATTIC – TO – BASEMENT:</h3>
          <ul><li>Sorting – Purging - Organizing</li></ul>
          <h3>PAPER CONTROL:</h3>
          <ul><li>Sorting – Purging - Organizing</li><li>Household, home office &amp; home based filing systems</li></ul>
          <h3>DOWNSIZING:</h3>
          <ul><li>Sorting – purging - organizing - labeling</li><li>Packing &amp; unpacking</li></ul>
        </div>
        <div class="services__col">
          <h3>REMOVAL:</h3>
          <ul><li>Light trash &amp; proper disposal</li><li>Donations &amp; light recyclables to proper locations</li><li>Shredding Service</li></ul>
          <h3>FOLLOW UP:</h3>
          <ul><li>Routine “clutter maintenance” visits</li></ul>
          <p class="note">For projects not listed above, please contact me.</p>
        </div>
      </div>
    </div>
  </section>

</main>
</body>
</html>
```